Flyer für Therapie- und Gesundheitsdienstleister
Zielgruppe
Therapie- und Gesundheitsdienstleister im Bereich Physiotherapie, Podologie, Prävention und betriebliche Gesundheitsförderung. Für dieses Projekt möchten wir einen Flyer erstellen lassen für die Bewerbung der betrieblichen Gesundheitsförderungen in bzw. für Firmen
Aufgabenstellung
Klare Strukturen, nicht verspielt, DINA4 oder DINA5; leicht medizinischer Touch, evntuell Stockfotos integrieren, edel und hochwertiges Design

```html
<!DOCTYPE html>
<html lang="de">
<head>
<meta charset="utf-8">
<title>Flyer Betriebliche Gesundheitsförderung</title>
<link href="https://fonts.googleapis.com/css2?family=Montserrat:wght@400;500;700;800&display=swap" rel="stylesheet">
<style>
  :root{
    --navy:#252a52;
    --rule:#5a5f78;
    --panel-left-a:#c9ccd9;
    --panel-left-b:#a9adbf;
    --panel-mid-a:#c4cfdc;
    --panel-mid-b:#aebdce;
    --photo-a:#8e8f93;
    --photo-b:#c9cbc8;
    --grey-text:#575b6e;
    --brand-grey:#555555;
    --brand-green:#4aa53a;
    --contact-band:#cde6c8;
    --icon-bg:#555a6e;
    --white:#ffffff;
  }
  *{margin:0;padding:0;box-sizing:border-box;}
  html,body{width:1200px;height:848px;overflow:hidden;background:var(--white);}
  body{font-family:"Montserrat",sans-serif;color:var(--navy);}
  .flyer{position:relative;width:1200px;height:848px;}
  .panel{position:absolute;top:0;height:848px;}
  .panel-left{left:0;width:400px;background:linear-gradient(160deg,var(--panel-left-a),var(--panel-left-b) 60%,#b9bccb);}
  .panel-mid{left:400px;width:395px;background:linear-gradient(170deg,var(--panel-mid-a),var(--panel-mid-b) 55%,#c7d0dc);}
  .panel-right{left:795px;width:405px;background:var(--white);}
  .abs{position:absolute;}
  h2{font-weight:800;font-size:37px;line-height:36px;color:var(--navy);letter-spacing:.2px;}
  .rule{position:absolute;height:1px;background:var(--rule);}
  .body{font-size:13.4px;line-height:20.4px;text-align:justify;color:var(--navy);}
  .list{list-style:none;font-size:13.4px;line-height:20.4px;}
  .list li{position:relative;padding-left:22px;text-align:justify;}
  .list li::before{content:"";position:absolute;left:3px;top:8px;width:4px;height:4px;border-radius:50%;background:var(--navy);}
  .brand{position:absolute;left:830px;top:44px;display:flex;align-items:center;gap:22px;}
  .brand-dot{width:60px;height:60px;border-radius:50%;background:var(--brand-green);}
  .brand-name{font-size:37px;line-height:47px;font-weight:400;color:var(--brand-grey);}
  .portrait{position:absolute;left:802px;top:182px;width:398px;height:458px;background:radial-gradient(ellipse at 50% 45%,var(--photo-b),var(--photo-a) 75%);}
  .claim{position:absolute;left:846px;top:556px;font-size:20.5px;font-weight:700;line-height:35px;color:var(--grey-text);letter-spacing:.3px;}
  .contact-band{position:absolute;left:802px;top:640px;width:398px;height:208px;background:var(--contact-band);}
  .contact{position:absolute;left:857px;display:flex;align-items:center;gap:24px;color:var(--white);}
  .contact .icon{width:36px;height:36px;border-radius:50%;background:var(--icon-bg);display:flex;align-items:center;justify-content:center;flex:none;}
  .contact .phone{font-size:20px;font-weight:500;}
  .contact .small{font-size:14px;font-weight:500;line-height:15px;text-transform:uppercase;}
</style>
</head>
<body>
<div class="flyer">
  <section class="panel panel-left" role="img" aria-label="Foto: Physiotherapeut behandelt den Rücken einer Patientin, bläulich überlagert"></section>
  <section class="panel panel-mid" role="img" aria-label="Foto: Patientin auf einer Behandlungsliege, bläulich überlagert"></section>
  <section class="panel panel-right"></section>

  <!-- Left panel -->
  <h2 class="abs" style="left:40px;top:41px;">Mentale<br>Gesundheit</h2>
  <div class="rule" style="left:40px;top:130px;width:283px;"></div>
  <p class="abs body" style="left:44px;top:177px;width:304px;">Programme zur Achtsamkeit, Entspannung, und Wahrnehmung. In Kleingruppen, Online oder als Einzelleistung buchbar</p>

  <h2 class="abs" style="left:44px;top:269px;">Digitaler<br>Gesundheits-<br>coach</h2>
  <div class="rule" style="left:44px;top:405px;width:283px;"></div>
  <ul class="abs list" style="left:44px;top:450px;width:304px;">
    <li>Workouts</li>
    <li>Live Online- Kurse</li>
    <li>Physio Übungen gezielt und individuell in der</li>
    <li>Einzelberatung online und persönlich abgestimmt</li>
    <li>Online Präventionscoach</li>
  </ul>

  <h2 class="abs" style="left:44px;top:612px;">Gesundheitstage<br>für Firmen</h2>
  <div class="rule" style="left:44px;top:711px;width:283px;"></div>
  <p class="abs body" style="left:44px;top:756px;width:304px;">Individuell auf Ihre Firma abgestimmt.</p>

  <!-- Middle panel -->
  <h2 class="abs" style="left:436px;top:33px;">Informationen<br>zu den Kosten</h2>
  <div class="rule" style="left:436px;top:131px;width:283px;"></div>
  <p class="abs body" style="left:436px;top:177px;width:303px;">Bis zu 600 € können Sie, als Arbeitgeber steuerfrei bezuschussen. Voraussetzung dafür ist, dass die fachlichen Anforderungen des GKV- Spitzenverbandes erfüllt werden. Diese Leistungen können wir erfüllen und einige mehr on Top. Lassen Sie sich persönlich und individuell beraten und nehmen Sie persönlich oder via E-Mail Kontakt mit uns auf. Senden Sie uns eine E-Mail an kontakt@physio-bewegt-lindenau.de und wir melden uns umgehend für eine kostenlose Beratung.</p>

  <h2 class="abs" style="left:444px;top:446px;">Über uns</h2>
  <div class="rule" style="left:444px;top:510px;width:283px;"></div>
  <p class="abs body" style="left:444px;top:555px;width:304px;">Physio Bewegt Lindenau ist eine Physiotherapie-Praxis in Lindenau, Deutschland, die sich auf die Behandlung von Schmerzen, Bewegungseinschränkungen und Verletzungen spezialisiert hat. Das Team besteht aus qualifizierten Physiotherapeuten, die individuelle Behandlungspläne für jeden Patienten erstellen, um eine optimale Genesung zu gewährleisten.</p>

  <!-- Right panel -->
  <div class="brand">
    <div class="brand-dot"></div>
    <div class="brand-name">Haus<br>Vitalis</div>
  </div>
  <div class="portrait" role="img" aria-label="Porträtfoto einer lächelnden Therapeutin in Praxiskleidung vor grauem Hintergrund"></div>
  <div class="claim">BETRIEBLICHE<br>GESUNDHEITSFÖRDERUNG</div>

  <div class="contact-band"></div>
  <div class="contact" style="top:675px;">
    <div class="icon">
      <svg width="18" height="18" viewBox="0 0 24 24"><path fill="#fff" d="M6.6 10.8a15.1 15.1 0 0 0 6.6 6.6l2.2-2.2c.3-.3.7-.4 1-.2 1.1.4 2.3.6 3.6.6.6 0 1 .4 1 1V20c0 .6-.4 1-1 1A17 17 0 0 1 3 4c0-.6.4-1 1-1h3.5c.6 0 1 .4 1 1 0 1.3.2 2.5.6 3.6.1.3 0 .7-.2 1z"/></svg>
    </div>
    <span class="phone">+49 2100 - 55 60 70</span>
  </div>
  <div class="contact" style="top:727px;">
    <div class="icon">
      <svg width="18" height="14" viewBox="0 0 20 14"><rect x="0" y="0" width="20" height="14" rx="2" fill="#fff"/><path d="M1 1l9 7 9-7" fill="none" stroke="#555a6e" stroke-width="1.6"/></svg>
    </div>
    <span class="small">kontakt@physio-bewegt-<br>lindenau.de</span>
  </div>
  <div class="contact" style="top:775px;">
    <div class="icon">
      <svg width="16" height="20" viewBox="0 0 16 20"><path fill="#fff" d="M8 0a7 7 0 0 0-7 7c0 5 7 13 7 13s7-8 7-13a7 7 0 0 0-7-7z"/><circle cx="8" cy="7" r="2.6" fill="#555a6e"/></svg>
    </div>
    <span class="small">Ahornweg 14a<br>12345 Lindenau</span>
  </div>
</div>
</body>
</html>
```